Lionel Arbusto and Dwight Halvorsen Advertisement

We would like an ad that conveys understated elegance. We are a company that purchases estate jewelry watches and diamonds. We care to a wealthy, upscale clientele.

Target Market(s)

Wealthy upscale.

Industry/Entity Type

It Company

Requirements
Must have
• Elegant Design. Crisp Clean. Attached a doc of how the ad should be arranged.

```html
<!DOCTYPE html>
<html lang="en">
<head>
<meta charset="UTF-8">
<title>Lionel Arbusto &amp; Dwight Halvorsen — Ready to Sell?</title>
<link rel="stylesheet" href="https://fonts.googleapis.com/css2?family=Cinzel:wght@400;500;600&display=swap">
<style>
  :root {
    --backdrop: #3b3c3d;
    --page-top: #dcdcdc;
    --page-mid: #cfcfcf;
    --page-low: #c6c6c6;
    --band: #f7f7f7;
    --ink: #1f1f1f;
    --ink-soft: #3a3a3a;
    --rule: #555555;
    --gem-light: #f4f4f4;
    --gem-mid: #c9c9c9;
    --gem-dark: #8e8e8e;
  }
  * { margin: 0; padding: 0; box-sizing: border-box; }
  html, body {
    width: 1200px;
    height: 900px;
    overflow: hidden;
    background: var(--backdrop);
  }
  .canvas {
    width: 1200px;
    height: 900px;
    display: flex;
    align-items: center;
    justify-content: center;
  }
  .ad-page {
    position: relative;
    width: 640px;
    height: 860px;
    background: linear-gradient(to bottom, var(--page-top) 0%, var(--page-mid) 45%, var(--page-low) 100%);
    font-family: "Cinzel", "Trajan Pro", serif;
    color: var(--ink);
    text-align: center;
    overflow: hidden;
  }
  .headline {
    position: absolute;
    top: 42px;
    left: 0;
    right: 0;
    font-size: 54px;
    font-weight: 500;
    letter-spacing: 1px;
    color: var(--ink);
    text-shadow: 0 1px 0 rgba(255,255,255,0.6);
  }
  .gem-photo {
    position: absolute;
    top: 140px;
    left: 50%;
    width: 220px;
    height: 200px;
    margin-left: -110px;
    border-radius: 8px;
    background: radial-gradient(ellipse at 45% 40%, var(--gem-light) 0%, var(--gem-mid) 55%, var(--gem-dark) 100%);
    box-shadow: 0 14px 18px -10px rgba(0,0,0,0.35);
  }
  .brand-band {
    position: absolute;
    top: 380px;
    left: 0;
    width: 640px;
    height: 220px;
  }
  .brand {
    position: absolute;
    top: 418px;
    left: 0;
    right: 0;
  }
  .brand-mark {
    display: block;
    width: 46px;
    height: 46px;
    margin: 0 auto 18px;
    border: 2px solid var(--ink);
  }
  .brand-names {
    font-size: 22px;
    font-weight: 500;
    letter-spacing: 0.5px;
    color: var(--ink);
  }
  .brand-tagline {
    display: flex;
    align-items: center;
    justify-content: center;
    gap: 10px;
    margin-top: 4px;
    font-size: 11px;
    letter-spacing: 1.5px;
    color: var(--ink-soft);
  }
  .brand-tagline::before,
  .brand-tagline::after {
    content: "";
    width: 140px;
    height: 1px;
    background: var(--rule);
  }
  .service {
    position: absolute;
    top: 610px;
    left: 0;
    right: 0;
  }
  .service-line {
    display: inline-block;
    padding: 0 6px 6px;
    border-bottom: 1px solid var(--rule);
    color: var(--ink-soft);
  }
  .service-line.discretion {
    font-size: 22px;
    letter-spacing: 1.5px;
  }
  .service-line.appointment {
    margin-top: 8px;
    font-size: 18px;
    letter-spacing: 6px;
  }
  .contact {
    position: absolute;
    top: 712px;
    left: 0;
    right: 0;
    font-style: normal;
    font-size: 14px;
    line-height: 20px;
    letter-spacing: 1.2px;
    color: var(--ink-soft);
  }
  .contact span { display: block; }
</style>
</head>
<body>
<main class="canvas">
  <article class="ad-page">
    <h1 class="headline">Ready to Sell?</h1>

    <div class="gem-photo" role="img" aria-label="Photograph of a large emerald-cut diamond"></div>

    <svg class="brand-band" viewBox="0 0 640 220" aria-hidden="true">
      <path d="M0,40 C180,-6 420,70 640,22 L640,178 C440,226 200,150 0,190 Z" fill="var(--band)"/>
    </svg>

    <div class="brand">
      <span class="brand-mark" aria-hidden="true"></span>
      <p class="brand-names">Lionel Arbusto &amp; Dwight Halvorsen</p>
      <p class="brand-tagline">Your Best Option</p>
    </div>

    <div class="service">
      <p><span class="service-line discretion">Utmost Discretion</span></p>
      <p><span class="service-line appointment">By Appointment</span></p>
    </div>

    <address class="contact">
      <span>Via Solana</span>
      <span>318-B Marlow Avenue</span>
      <span>Harbor Point, FL 33999</span>
      <span>support@arbustohalvorsen.com</span>
      <span>555.014.2290</span>
    </address>
  </article>
</main>
</body>
</html>
```